Business Card Design

We are a family run drainage & groundworks company that specialise in treatment plant installation. We work for commercial & domestic property's, we have specialised knowledge & equipment for CCTV surveys, jetting blockages & repairing all types of drainage systems.

Industry/Entity Type

Business

Contact Information for Business Card

14 Marlpit Workshops
Belcombe Mill Lane
Fordingbridge
Hampshire
SP4 7TN
Tel: 01632 960418
Fax: 01632 960752
Mobile: 07700 900318
enquiries@kestrelwd.co.uk
www.kestrelwastedrainage.co.uk

Requirements
Must have
• logo, address, the right colour green.
I need the cards to also have individuals names:

Tom lydgate
Neil Carrow
Helen Lydgate
Di Pemberton

And also some with just the name & address on :)

```html
<!DOCTYPE html>
<html lang="en">
<head>
<meta charset="utf-8">
<title>Kestrel Waste &amp; Drainage – Business Card</title>
<link rel="stylesheet" href="https://fonts.googleapis.com/css2?family=Ubuntu:wght@400;700&display=swap">
<style>
  :root {
    --page-bg: #f2f2f2;
    --card-bg: #ffffff;
    --green-dark: #00923f;
    --green-light: #8dc63f;
    --text-white: #ffffff;
    --shadow: rgba(0, 0, 0, 0.18);
  }
  * { margin: 0; padding: 0; box-sizing: border-box; }
  html, body {
    width: 1200px;
    height: 1200px;
    overflow: hidden;
    background: var(--page-bg);
    font-family: "Ubuntu", sans-serif;
  }
  .card {
    position: absolute;
    left: 145px;
    top: 342px;
    width: 897px;
    height: 499px;
    background: var(--card-bg);
    box-shadow: 0 4px 10px var(--shadow);
    overflow: hidden;
  }
  .card-shapes {
    position: absolute;
    inset: 0;
    width: 897px;
    height: 499px;
  }
  .brand {
    position: absolute;
    left: 48px;
    top: 140px;
    display: flex;
    align-items: center;
    gap: 18px;
  }
  .brand-square {
    width: 56px;
    height: 56px;
    background: var(--green-dark);
    flex: none;
  }
  .brand-name {
    font-weight: 700;
    font-size: 29px;
    line-height: 1.15;
    color: var(--green-dark);
  }
  .person-name {
    position: absolute;
    right: 17px;
    top: 84px;
    font-weight: 700;
    font-size: 43px;
    line-height: 1;
    color: var(--green-dark);
  }
  .contact {
    position: absolute;
    right: 17px;
    top: 172px;
    text-align: right;
    color: var(--text-white);
    font-size: 21px;
    line-height: 28.6px;
  }
  .address { font-weight: 700; }
  .numbers { font-weight: 400; }
  .website {
    position: absolute;
    right: 17px;
    top: 425px;
    font-weight: 700;
    font-size: 22px;
    color: var(--text-white);
  }
</style>
</head>
<body>
  <article class="card">
    <svg class="card-shapes" viewBox="0 0 897 499">
      <rect role="img" aria-label="Light green grass illustration along the bottom left"
            fill="var(--green-light)" x="0" y="383" width="440" height="116"/>
      <rect role="img" aria-label="Dark green hedge illustration at the top right"
            fill="var(--green-dark)" x="556" y="0" width="341" height="73"/>
      <rect role="img" aria-label="Dark green tree illustration filling the right side"
            fill="var(--green-dark)" x="380" y="141" width="517" height="358"/>
    </svg>

    <div class="brand">
      <span class="brand-square"></span>
      <span class="brand-name">Kestrel Waste<br>&amp; Drainage</span>
    </div>

    <h1 class="person-name">Tom lydgate</h1>

    <div class="contact">
      <p class="address">14 Marlpit Workshops<br>Belcombe Mill Lane<br>Fordingbridge<br>Hampshire SP4 7TN</p>
      <p class="numbers">T : 01632 960418<br>F : 01632 960752<br>M : 07700 900318<br>E : enquiries@kestrelwd.co.uk</p>
    </div>

    <p class="website">www.kestrelwastedrainage.co.uk</p>
  </article>
</body>
</html>
```